Business Card Design - front and back

Residential real estate agent looking for a an emphasis on my first name (last name is hard to spell).  Would love the slogan "It's more than a contract" on the card.  Simple, easy to read business card that makes people want to pick it up and remember it.  The Bright Gable Properties has to be on the front of card but does not need to be the emphasis.  Prefer locations on the back.  Would love a home on it.  Looking for simply elegant in the card that shows I am a non-complicated, warm, honest real estate agent.
NEED ONE OF MY PICTURES ON THE CARD.  LEAVING WHICH ONE UP TO THE DESIGNER.

Industry/Entity Type
Real Estate
Contact Information for Business Card
Marla Quist, Broker Associate, Bright Gable Properties, 727-555-0148 cell, callmemarla@example.net, listedwithmarla.example, Bright Gable Properties locations: 48215 Pellory Blvd Ste 101, Tampa, FL  33999, 2918 Vossin Ct Ste 101, New Port Richey, FL  34999
I NEED THIS DOUBLE SIDED - THE SELECTION BELOW WILL NOT ALLOW IT?
Requirements
Must have
- Emphasis on my first name
a home in it
LOVE Gloria Padgett's logo which sits on the left side in the margin at
http://gloriapadgett.sampleagentsite.example/
Something with that idea is exactly what I am looking for.
Nice to have
- Nice script that is readable.
Should not have
- I am looking for something simple

```html
<!DOCTYPE html>
<html lang="en">
<head>
<meta charset="utf-8">
<title>Marla Quist – Business Card, Front and Back</title>
<link rel="stylesheet" href="https://fonts.googleapis.com/css2?family=Great+Vibes&family=Questrial&display=swap">
<style>
  :root {
    --backdrop: #e9e6e1;
    --card-white: #ffffff;
    --ink: #1c1c1c;
    --ink-soft: #2e2e2e;
    --photo-dark: #1d2226;
    --photo-mid: #4a4f4c;
    --photo-warm: #8a7a52;
    --photo-light: #cfcabd;
    --slogan: #f3f1ec;
    --logo-light: #ffffff;
    --card-shadow: 0 10px 28px rgba(0,0,0,0.18);
  }
  * { box-sizing: border-box; margin: 0; padding: 0; }
  html, body {
    width: 1200px; height: 723px; overflow: hidden;
    background: var(--backdrop);
  }
  .canvas {
    position: relative; width: 1200px; height: 723px;
    display: flex; justify-content: center; align-items: center; gap: 60px;
  }
  .card {
    position: relative; width: 360px; height: 630px;
    box-shadow: var(--card-shadow); overflow: hidden;
  }

  /* Back side: contact details */
  .card-back {
    background: var(--card-white); color: var(--ink);
    font-family: "Questrial", sans-serif;
    padding: 44px 34px 0 36px;
  }
  .logo-name {
    display: flex; align-items: center; gap: 12px;
    font-size: 34px; color: var(--ink); margin-left: 40px;
  }
  .logo-mark { width: 16px; height: 16px; background: var(--ink); flex: none; }
  .title-block { margin-top: 16px; margin-left: 56px; font-size: 18px; line-height: 1.2; color: var(--ink-soft); }
  .contact { margin-top: 44px; font-size: 17px; line-height: 1.55; color: var(--ink-soft); }
  .locations-head { margin-top: 34px; font-size: 15px; font-weight: bold; color: var(--ink); }
  .address { margin-top: 18px; font-size: 17px; line-height: 1.45; color: var(--ink-soft); }
  .address + .address { margin-top: 6px; }

  /* Front side: photograph with slogan */
  .card-front { background: var(--photo-dark); }
  .photo {
    position: absolute; inset: 0;
    background:
      linear-gradient(90deg, var(--photo-light) 0%, var(--photo-light) 22%, var(--photo-dark) 30%, var(--photo-dark) 88%, var(--photo-mid) 100%),
      var(--photo-dark);
  }
  .photo::after {
    content: ""; position: absolute; left: 0; right: 0; bottom: 0; height: 32%;
    background: linear-gradient(180deg, rgba(138,122,82,0) 0%, var(--photo-warm) 35%, var(--photo-mid) 100%);
  }
  .slogan {
    position: absolute; top: 18px; right: 22px;
    font-family: "Great Vibes", cursive; font-size: 30px; color: var(--slogan);
  }
  .front-logo {
    position: absolute; left: 0; right: 0; bottom: 46px;
    display: flex; justify-content: center; align-items: center; gap: 12px;
    font-family: "Questrial", sans-serif; font-size: 36px; color: var(--logo-light);
  }
  .front-logo .logo-mark { background: var(--logo-light); }
</style>
</head>
<body>
<main class="canvas">
  <section class="card card-back" aria-label="Card back">
    <div class="logo-name"><span class="logo-mark"></span>Marla Quist</div>
    <div class="title-block">
      <p>Broker Associate</p>
      <p>Bright Gable Properties</p>
    </div>
    <div class="contact">
      <p>727-555-0148</p>
      <p>callmemarla@example.net</p>
      <p>listedwithmarla.example</p>
    </div>
    <p class="locations-head">Bright Gable Properties Locations</p>
    <p class="address">48215 Pellory Blvd<br>Ste 101, Tampa, FL 33999,</p>
    <p class="address">2918 Vossin Ct, Ste 101<br>New Port Richey, FL 34999</p>
  </section>

  <section class="card card-front" aria-label="Card front">
    <div class="photo" role="img" aria-label="Photograph of a dark front door on a white porch with a potted plant and doormat"></div>
    <p class="slogan">It's more than a contract</p>
    <div class="front-logo"><span class="logo-mark"></span>Marla Quist</div>
  </section>
</main>
</body>
</html>
```